We are a full service general contractor that specializes in emergency services and insurance restoration/repair. Most of our work relates to water damage, fire dame, smoke, wind and hail, storm damage, etc. Pretty much anything you would call your insurance company for.

On one side of card the logo is VERY easy with the possibility of some modifications once I get a preview. I had a logo designed years ago and its on all my vehicles so I want to stick with my branding at this point and time.

Its a 2 sided card-for one side I would like the following:
* See logo (its attached)
* I would like this logo as large/big/bold as possible-essentially it should fill up the entire side of the card (barring it not looking proportionally correct of course)
* I think the background should be white behind it-or possibly red (with colors inverted so that they don't get lost in the red background)
* I'm attaching a photo of one of our work vans to go off of-you will notice that the .com wraps up the side of the logo-this .com portion needs to added on as the logo is only the crest renewal logo

The other side of the card I'm thinking should be:
* My biggest struggle is formatting-in other words-I don't know how to lay out all that info without the card looking jumbled/messy
* all our logos, vehicles, marketing media, etc. is based on or at least inspired by a clean look
* a smaller version of logo (without the .com) should be located somewhere on this side of card-I've seen some cards where its centered and others where its offset-I'm not sure which is better
* I could conceivably leave off PO BOX if its too much info and something needs deleted

The logo will display company name-other pertinent info:
Phone: 704 555 0183
Mobile: 704 555 0147
Fax: 704 555 0192
email: crestrenewal@mailhub.example
Address: 2583 Elm Rd.
Charlotte, NC
PO BOX 36502 28299

```html
<!DOCTYPE html>
<html lang="en">
<head>
<meta charset="utf-8">
<title>Crest Renewal – Business Card</title>
<link rel="stylesheet" href="https://fonts.googleapis.com/css2?family=Open+Sans:wght@400;600;700;800&display=swap">
<style>
  :root {
    --slate: #3f5866;
    --red: #c0161e;
    --white: #ffffff;
    --backdrop: #e6e7e8;
    --shadow: rgba(0, 0, 0, 0.18);
  }
  * { box-sizing: border-box; margin: 0; padding: 0; }
  html, body {
    width: 1200px;
    height: 900px;
    overflow: hidden;
    background: var(--backdrop);
    font-family: "Open Sans", Arial, sans-serif;
  }
  .canvas {
    position: relative;
    width: 1200px;
    height: 900px;
  }
  .card {
    position: absolute;
    width: 640px;
    height: 366px;
    background: var(--white);
    box-shadow: 0 6px 18px var(--shadow);
    overflow: hidden;
  }
  .card--front { left: 280px; top: 58px; }
  .card--back  { left: 280px; top: 474px; display: flex; }

  /* Front: large wordmark */
  .front-mark {
    position: absolute;
    inset: 0;
    display: flex;
    align-items: center;
    justify-content: center;
    gap: 22px;
  }
  .mark-square {
    width: 58px;
    height: 58px;
    background: var(--red);
    flex: none;
  }
  .front-name {
    font-weight: 800;
    font-size: 56px;
    line-height: 0.98;
    color: var(--slate);
    letter-spacing: 1px;
  }

  /* Back: logo strip */
  .back-logo {
    position: relative;
    width: 218px;
    height: 100%;
    flex: none;
    background: var(--white);
    border-right: 5px solid var(--red);
  }
  .back-logo__inner {
    position: absolute;
    left: 50%;
    top: 50%;
    transform: translate(-50%, -50%) rotate(-90deg);
    display: flex;
    align-items: center;
    gap: 12px;
    white-space: nowrap;
  }
  .back-logo .mark-square { width: 30px; height: 30px; }
  .back-name {
    font-weight: 800;
    font-size: 34px;
    line-height: 1;
    color: var(--slate);
    letter-spacing: 0.5px;
  }

  /* Back: contact panel */
  .contact {
    flex: 1;
    background: var(--slate);
    color: var(--white);
    padding: 78px 0 0 52px;
  }
  .contact__name {
    font-weight: 700;
    font-size: 27px;
    letter-spacing: 1.5px;
    line-height: 1.1;
  }
  .contact__role {
    font-size: 13px;
    letter-spacing: 1.5px;
    margin-top: 2px;
  }
  .contact__address {
    font-size: 15px;
    line-height: 1.3;
    margin-top: 16px;
  }
  .contact__list {
    list-style: none;
    margin-top: 12px;
    font-size: 15px;
    line-height: 1.35;
  }
  .contact__list li {
    display: flex;
    align-items: center;
    gap: 9px;
  }
  .contact__icon {
    width: 12px;
    height: 12px;
    flex: none;
    fill: var(--white);
  }
</style>
</head>
<body>
<main class="canvas">

  <section class="card card--front" aria-label="Card front">
    <div class="front-mark">
      <span class="mark-square" aria-hidden="true"></span>
      <p class="front-name">CREST<br>RENEWAL</p>
    </div>
  </section>

  <section class="card card--back" aria-label="Card back">
    <div class="back-logo">
      <div class="back-logo__inner">
        <span class="mark-square" aria-hidden="true"></span>
        <span class="back-name">CREST RENEWAL</span>
      </div>
    </div>

    <div class="contact">
      <h1 class="contact__name">DALE HARKER</h1>
      <p class="contact__role">DIRECTOR</p>
      <p class="contact__address">2583 Elm Rd. Charlotte<br>NC PO BOX 36502 28299</p>
      <ul class="contact__list">
        <li>
          <svg class="contact__icon" viewBox="0 0 24 24" aria-hidden="true"><path d="M6.6 10.8a15.1 15.1 0 0 0 6.6 6.6l2.2-2.2c.3-.3.7-.4 1-.2 1.1.4 2.3.6 3.6.6.6 0 1 .4 1 1V20c0 .6-.4 1-1 1C10.6 21 3 13.4 3 4c0-.6.4-1 1-1h3.5c.6 0 1 .4 1 1 0 1.3.2 2.5.6 3.6.1.3 0 .7-.2 1z"/></svg>
          <span>704 555 0183</span>
        </li>
        <li>
          <svg class="contact__icon" viewBox="0 0 24 24" aria-hidden="true"><path d="M7 1h10a2 2 0 0 1 2 2v18a2 2 0 0 1-2 2H7a2 2 0 0 1-2-2V3a2 2 0 0 1 2-2zm0 3v14h10V4zm5 15.2a1.2 1.2 0 1 0 0 2.4 1.2 1.2 0 0 0 0-2.4z"/></svg>
          <span>704 555 0147</span>
        </li>
        <li>
          <svg class="contact__icon" viewBox="0 0 24 24" aria-hidden="true"><path d="M6 2h9l3 3v5H6zM3 11h18a1 1 0 0 1 1 1v8a1 1 0 0 1-1 1H3a1 1 0 0 1-1-1v-8a1 1 0 0 1 1-1zm3 3v2h2v-2zm4 0v2h2v-2zm4 0v2h4v-2z"/></svg>
          <span>704 555 0192</span>
        </li>
        <li>
          <svg class="contact__icon" viewBox="0 0 24 24" aria-hidden="true"><path d="M2 5h20v14H2zm2 2v.5l8 5.5 8-5.5V7zm0 2.9V17h16V9.9l-8 5.5z"/></svg>
          <span>crestrenewal@mailhub.example</span>
        </li>
      </ul>
    </div>
  </section>

</main>
</body>
</html>
```